Company Flyer for Electric boating company

I am looking for a company flyer which we can hand over to boat owners in the Netherlands (Amsterdam area). Our core business is to rebuild every boat (from 4 to 10 meters) into an electrically propelled boat. We are taking out diesels and replace them with a high quality electrical motor, inboard varying from 30 till 80 pk (hp). And outboard from 1pk (hp) till 200pk. We are the best, not the cheapest, not the most expensive. We only work with the best materials. The flyer has to be sort of in line with our website and branding.

Major advantages of electric boating are:
- completely silent
- no fumes, smells or smoke
- cheap to operate
- environmentally friendly
- obliged in more and more areas
- no maintenance
- more enjoyable

The flyer should be A5 format. Since all the text has to be in Dutch I expect only the graphical design and layout for advantages, process, pricing and contact details etc.

Target Market(s)

Boat owners in the Netherlands

Font styles to use
Sans Serif

Colors
9bcb3c
add136
cadf82
0555a3
3176b5
85acd3
e0ebf3

Requirements
Must have
• Clean design, in line with website: www.stroomkade.nl
Nice to have
• icons for advantages, boating etc

2 sides
Should not have
• Steering wheel...

```html
<!DOCTYPE html>
<html lang="nl">
<head>
<meta charset="utf-8">
<title>Stroomkade – Flyer elektrisch varen</title>
<link href="https://fonts.googleapis.com/css2?family=Arimo:wght@400;700&family=Bebas+Neue&family=Oswald:wght@500;600&display=swap" rel="stylesheet">
<style>
  :root{
    --stage:#2c3040;
    --green:#7dbb2f;
    --green-light:#9bcb3c;
    --ink:#3a3d4c;
    --text:#3d4050;
    --paper:#f1f2f2;
    --white:#ffffff;
    --water-dark:#1f3a52;
    --water:#3b6a86;
    --hill:#3d5a4a;
    --sky:#7d8a90;
  }
  *{box-sizing:border-box;margin:0;padding:0}
  html,body{width:1200px;height:1200px;overflow:hidden;background:var(--stage)}
  .flyer{position:absolute;left:240px;top:40px;width:720px;height:1120px;background:var(--paper);overflow:hidden;font-family:"Arimo",Arial,sans-serif;color:var(--text)}
  .hero-photo{position:absolute;left:0;top:0;width:720px;height:640px;
    background:linear-gradient(180deg,var(--sky) 0%,#5f7470 18%,var(--hill) 30%,#6b6a58 40%,var(--water) 48%,var(--water-dark) 75%,#18304a 100%)}
  .wave{position:absolute;left:0;top:0}
  .headline{position:absolute;left:70px;top:130px;color:var(--white)}
  .headline .small{font-size:40px;line-height:1;letter-spacing:.5px}
  .headline .boot{font-family:"Bebas Neue",Impact,sans-serif;font-size:168px;line-height:.85;color:var(--green);margin:6px 0 4px}
  .headline .indent{padding-left:22px}
  .brand-badge{position:absolute;left:450px;top:245px;width:230px;height:230px;border-radius:50%;border:7px solid var(--green);background:var(--water-dark);display:flex;align-items:center;justify-content:center}
  .brand-badge span{font-family:"Oswald",sans-serif;font-weight:600;font-size:36px;color:var(--green);letter-spacing:1px}
  .advantages-tab{position:absolute;left:500px;top:588px;width:220px;height:70px;background:var(--green);border-radius:35px 0 0 35px;display:flex;align-items:center;padding-left:36px;font-family:"Oswald",sans-serif;font-weight:500;font-size:19px;line-height:1.1;color:var(--white)}
  .intro{position:absolute;left:50px;top:655px;width:420px}
  .intro h2{font-size:30px;font-weight:700;line-height:1.12;color:var(--green);margin-bottom:18px}
  .intro p{font-size:14px;line-height:1.6}
  .contact{position:absolute;left:0;top:885px;width:490px;height:165px;background:var(--ink);border-radius:0 82px 82px 0;padding:20px 0 0 60px;color:var(--white)}
  .contact h3{font-family:"Oswald",sans-serif;font-weight:500;font-size:25px;line-height:1.2;color:var(--green);margin-bottom:6px}
  .contact .address{font-size:19px;line-height:1.35}
  .contact .phone{font-family:"Oswald",sans-serif;font-weight:600;font-size:34px;line-height:1.1;margin-top:4px}
  .benefits{position:absolute;left:520px;top:675px;width:190px;list-style:none}
  .benefits li{display:flex;align-items:center;gap:12px;padding:6px 0 7px;position:relative;font-family:"Oswald",sans-serif;font-weight:500;font-size:14px;line-height:1.25;color:var(--ink)}
  .benefits li::after{content:"";position:absolute;left:44px;bottom:0;width:64px;height:2px;background:var(--ink)}
  .benefits li:last-child::after{display:none}
  .benefits .icon{flex:0 0 32px;width:32px;height:32px;border-radius:50%;background:var(--green);display:flex;align-items:center;justify-content:center}
  .footer-band{position:absolute;left:0;bottom:0;width:720px;height:60px;background:var(--green);display:flex;align-items:center;justify-content:flex-end;padding-right:40px;font-size:27px;color:var(--ink)}
</style>
</head>
<body>
<main class="flyer">
  <div class="hero-photo" role="img" aria-label="Foto van een jachthaven met zeilboten, beboste bergen en water"></div>
  <svg class="wave" width="720" height="700" viewBox="0 0 720 700" aria-hidden="true">
    <path d="M0,565 C150,540 300,555 420,590 C520,620 560,580 590,500 C620,400 660,280 720,230 L720,700 L0,700 Z" fill="var(--paper)"/>
    <path d="M20,585 C150,565 300,580 420,615 C480,632 510,628 530,620" fill="none" stroke="var(--green)" stroke-width="7" stroke-linecap="round" stroke-dasharray="0 19"/>
    <path d="M640,450 C660,330 690,280 715,255" fill="none" stroke="var(--green)" stroke-width="5" stroke-linecap="round" stroke-dasharray="0 16"/>
    <path d="M565,478 L561,588" fill="none" stroke="var(--green)" stroke-width="10" stroke-linecap="round" stroke-dasharray="0 20"/>
  </svg>

  <div class="headline">
    <div class="small">Geef uw</div>
    <div class="boot">BOOT</div>
    <div class="small indent">een nieuwe</div>
    <div class="small indent">identiteit</div>
  </div>

  <div class="brand-badge"><span>STROOMKADE</span></div>

  <div class="advantages-tab">VOORDELEN VAN<br>ELEKTRISCH VAREN</div>

  <section class="intro">
    <h2>STROOMKADE<br>VERBOUWT BOTEN</h2>
    <p>Stroomkade is een scheepswerf in Amsterdam met als een van de kernactiviteiten het ombouwen van bestaande, traditioneel aangedreven, boten naar elektrische voortstuwing. Hier ligt een grote ambitie en deze sluit tevens aan bij het voornemen van de gemeente Amsterdam om vanaf 2025 alle beweging op het water uitstootvrij te laten plaatsvinden</p>
  </section>

  <section class="contact">
    <h3>VOOR MEER INFO CONTACT</h3>
    <div class="address">Havenstraat 42A 1021XK<br>Amsterdam (Noord) Nederland</div>
    <div class="phone">+31 6 18 402 957</div>
  </section>

  <ul class="benefits">
    <li><span class="icon"><svg width="18" height="18" viewBox="0 0 18 18" fill="none" stroke="var(--ink)" stroke-width="1.6"><path d="M3 7h3l4-3v10l-4-3H3z"/><path d="M2 2l14 14"/></svg></span>HELEMAAL STIL</li>
    <li><span class="icon"><svg width="18" height="18" viewBox="0 0 18 18" fill="none" stroke="var(--ink)" stroke-width="1.6"><path d="M4 13a3 3 0 0 1 1-6 4 4 0 0 1 8 1 2.5 2.5 0 0 1 0 5z"/><path d="M2 2l14 14"/></svg></span>GEEN DAMPEN,<br>GEUREN OF ROOK</li>
    <li><span class="icon"><svg width="18" height="18" viewBox="0 0 18 18" fill="none" stroke="var(--ink)" stroke-width="1.6"><circle cx="9" cy="9" r="6.5"/><path d="M11 6.5H8a1.5 1.5 0 0 0 0 3h2a1.5 1.5 0 0 1 0 3H7M9 5v8"/></svg></span>GOEDKOOP TE BEDIENEN</li>
    <li><span class="icon"><svg width="18" height="18" viewBox="0 0 18 18" fill="none" stroke="var(--ink)" stroke-width="1.6"><path d="M3 15C3 7 8 3 15 3c0 7-4 12-12 12z"/><path d="M3 15l7-7"/></svg></span>MILIEUVRIENDELIJK</li>
    <li><span class="icon"><svg width="18" height="18" viewBox="0 0 18 18" fill="none" stroke="var(--ink)" stroke-width="1.8"><path d="M4 9l3.5 3.5L14 5"/></svg></span>VERPLICHT OP STEEDS<br>MEER GEBIEDEN</li>
    <li><span class="icon"><svg width="18" height="18" viewBox="0 0 18 18" fill="none" stroke="var(--ink)" stroke-width="1.6"><path d="M12 2a3.5 3.5 0 0 0-3 5L3 13l2 2 6-6a3.5 3.5 0 0 0 5-3l-2 1-2-2z"/></svg></span>GEEN ONDERHOUD</li>
    <li><span class="icon"><svg width="18" height="18" viewBox="0 0 18 18" fill="none" stroke="var(--ink)" stroke-width="1.6"><circle cx="9" cy="9" r="6.5"/><path d="M6 10.5a3.5 3.5 0 0 0 6 0"/><circle cx="6.7" cy="7" r=".6" fill="var(--ink)"/><circle cx="11.3" cy="7" r=".6" fill="var(--ink)"/></svg></span>LEUKER</li>
  </ul>

  <footer class="footer-band">www.stroomkade.nl | info@stroomkade.nl</footer>
</main>
</body>
</html>
```